Inviting A6 Flyer for Church membership

We need an A6 size flyer for the church. We are looking for something fresh, inviting and impactful. Church new logo and current flyer design attached.
Back text as follows:
We would love to have you join us as our SPECIAL GUEST this Sunday at 10am.
You can find us at Harvest Lantern Family Church, 17-19 Marlow Crest Road
(Behind Brivo), Thornbury Meadow Village,QX4 7LB
For more information or for a chat, please call us on 07700 900418 / 07700 900752 or email church@hlfcuk-mail.test
Target Market(s)
Church
Industry/Entity Type
Church
Colors
Designer to choose colors to be used in the design.
Requirements
Must have
- fresh, inviting and impactful.
- Chruch logo (attached)
Should not have
- Too much going on

```html
<!DOCTYPE html>
<html lang="en">
<head>
<meta charset="utf-8">
<title>Be Our Guest – A6 Flyer</title>
<link href="https://fonts.googleapis.com/css2?family=Montserrat:wght@500;600;800&family=Great+Vibes&display=swap" rel="stylesheet">
<style>
  :root {
    --page-bg: #e6e7e9;
    --card-white: #ffffff;
    --teal: #1f5660;
    --accent-red: #a3171c;
    --guest-ice: #dbe6ef;
    --peak-top: #c9d3e4;
    --peak-mid: #6d7fa2;
    --peak-deep: #1e2c52;
    --haze-pink: #f4dbe6;
    --haze-lilac: #b7a9cb;
    --haze-deep: #4b5074;
  }
  * { box-sizing: border-box; margin: 0; padding: 0; }
  html, body { width: 1200px; height: 912px; overflow: hidden; }
  body {
    background: var(--page-bg);
    font-family: "Montserrat", Arial, sans-serif;
    position: relative;
  }
  .flyer {
    position: absolute;
    left: 340px;
    width: 520px;
    height: 368px;
    background: var(--card-white);
    padding: 11px;
    box-shadow: 0 6px 18px rgba(0,0,0,0.12);
  }
  .flyer--front { top: 60px; }
  .flyer--back { top: 484px; }
  .flyer__face {
    position: relative;
    width: 100%;
    height: 100%;
    overflow: hidden;
  }
  .scene { position: absolute; inset: 0; }
  .scene--peak {
    background: linear-gradient(180deg, var(--peak-top) 0%, #d9dfeb 35%, var(--peak-mid) 55%, var(--peak-deep) 100%);
  }
  .scene--valley {
    background: linear-gradient(180deg, #f2e9f4 0%, var(--haze-pink) 30%, var(--haze-lilac) 58%, var(--haze-deep) 100%);
  }
  .church-name {
    position: absolute;
    left: 0;
    right: 0;
    top: 34px;
    text-align: center;
    font-family: "Montserrat", Arial, sans-serif;
    font-weight: 600;
    font-size: 13px;
    letter-spacing: 0.3px;
    color: var(--teal);
    white-space: nowrap;
  }
  .headline {
    position: absolute;
    left: 0;
    right: 0;
    bottom: 58px;
    text-align: center;
    color: var(--guest-ice);
  }
  .headline__script {
    display: block;
    font-family: "Great Vibes", cursive;
    font-size: 44px;
    font-weight: 400;
    line-height: 1;
    color: #f3f6fa;
    margin-bottom: -8px;
  }
  .headline__main {
    display: block;
    font-weight: 800;
    font-size: 68px;
    letter-spacing: 3px;
    line-height: 1;
  }
  .invite {
    position: absolute;
    left: 0;
    right: 0;
    top: 72px;
    text-align: center;
    color: var(--teal);
  }
  .invite__lead {
    font-size: 15px;
    font-weight: 600;
    line-height: 1.3;
  }
  .invite__lead .accent { color: var(--accent-red); }
  .invite__lead .strong { font-size: 17px; }
  .invite__find {
    margin-top: 10px;
    font-size: 12px;
    font-weight: 600;
    color: var(--accent-red);
  }
  .invite__address {
    font-size: 12px;
    font-weight: 600;
    line-height: 1.35;
  }
  .invite__contact {
    margin-top: 16px;
    font-size: 11px;
    font-weight: 500;
    line-height: 1.45;
    color: #ffffff;
  }
</style>
</head>
<body>

  <section class="flyer flyer--front" aria-label="Flyer front">
    <div class="flyer__face">
      <div class="scene scene--peak" role="img" aria-label="Photograph of a snow-capped mountain peak rising through cloud"></div>
      <p class="church-name">Harvest Lantern Ministries</p>
      <h1 class="headline">
        <span class="headline__script">Be Our</span>
        <span class="headline__main">GUEST</span>
      </h1>
    </div>
  </section>

  <section class="flyer flyer--back" aria-label="Flyer back">
    <div class="flyer__face">
      <div class="scene scene--valley" role="img" aria-label="Illustration of misty layered hills and tree silhouettes under a soft sun"></div>
      <p class="church-name">Harvest Lantern Ministries</p>
      <div class="invite">
        <p class="invite__lead">
          We would love to have you join us as<br>
          <span class="accent strong">our SPECIAL GUEST this</span><br>
          <span class="strong">Sunday at 10am</span>
        </p>
        <p class="invite__find">You can find us at</p>
        <p class="invite__address">
          Harvest Lantern Family Church,<br>
          17-19 Marlow Crest Road (Behind Brivo),<br>
          Thornbury Meadow Village, QX4 7LB
        </p>
        <p class="invite__contact">
          For more information or for a chat,<br>
          please call us on<br>
          07700 900418 / 07700 900752 or email church@hlfcuk-mail.test
        </p>
      </div>
    </div>
  </section>

</body>
</html>
```